Ferncrest Dental, LLC business card project

Business card to be designed with current logo.
Dental office- please keep design of card that looks clean and professional.
Please include the following info:
Ferncrest Dental, LLC
Dr. Lorna Pettigrew
2871 Marlowe Street
Bethlehem, PA 18093
610-555-0193
ferncrestdental.office@examplemail.test
Hello everyone-
Reason: Just got back from overseas- will look at all designs and provide feedback. Thank you!
Reason: Polling my friends for the final selection-
thank you to all those that participated- so many talented designers!

```html
<!DOCTYPE html>
<html lang="en">
<head>
<meta charset="utf-8">
<title>Ferncrest Dental, LLC – Business Card</title>
<link rel="stylesheet" href="https://fonts.googleapis.com/css2?family=Quicksand:wght@400;500&family=Exo+2:wght@700;800&display=swap">
<style>
  :root {
    --page: #e8e5e0;
    --card-dark: #1f1f1d;
    --card-mid: #3e3e3c;
    --card-back: #25251f;
    --strip: #232323;
    --orange: #f57d0a;
    --orange-soft: #c9600c;
    --green: #6aab3c;
    --green-name: #5d9e3a;
    --lime: #a9d22c;
    --text-light: #e6e6e6;
    --text-muted: #cfcfcf;
    --silver: #ececec;
  }
  * { box-sizing: border-box; margin: 0; padding: 0; }
  html, body {
    width: 1200px; height: 1000px; overflow: hidden;
    background: var(--page);
  }
  .card {
    position: absolute;
    width: 756px; height: 427px;
    overflow: hidden;
    box-shadow: 0 6px 14px rgba(0,0,0,0.35);
    font-family: "Quicksand", sans-serif;
  }

  /* ---------- Front ---------- */
  .card--front {
    left: 27px; top: 25px;
    background: radial-gradient(ellipse 60% 70% at 48% 62%, var(--card-mid) 0%, var(--card-dark) 75%);
  }
  .brand {
    position: absolute; display: flex; align-items: center;
    color: var(--green); font-weight: 500; white-space: nowrap;
  }
  .brand__dot { border-radius: 50%; background: var(--green); flex: none; }
  .card--front .brand { left: 8px; top: 34px; font-size: 34px; gap: 12px; }
  .card--front .brand__dot { width: 34px; height: 34px; }
  .divider-v {
    position: absolute; left: 439px; top: 16px;
    width: 2px; height: 84px; background: var(--text-muted);
  }
  .doctor-front {
    position: absolute; left: 456px; top: 46px; width: 290px;
    font-family: "Exo 2", sans-serif; font-weight: 800;
    font-size: 25px; color: var(--silver);
    text-shadow: 0 2px 3px rgba(0,0,0,0.7);
    white-space: nowrap;
  }
  .location { position: absolute; left: 33px; top: 184px; color: var(--text-light); }
  .location__label { display: flex; align-items: center; gap: 4px; font-size: 15px; }
  .location__label svg { width: 10px; height: 10px; }
  .location__lines { margin: 11px 0 0 20px; font-size: 15.5px; line-height: 21px; color: var(--text-muted); }
  .arrows-art {
    position: absolute; left: 560px; top: 205px; width: 196px; height: 136px;
    background: radial-gradient(ellipse at 45% 80%, rgba(245,125,10,0.55), rgba(201,96,12,0.15) 55%, transparent 75%);
  }
  .band {
    position: absolute; left: 0; top: 340px; width: 756px; height: 32px;
    background: var(--orange);
  }
  .contact-strip {
    position: absolute; left: 0; top: 372px; width: 756px; height: 55px;
    background: var(--strip);
    display: flex; align-items: center; gap: 52px; padding-left: 30px;
    color: var(--text-light); font-size: 19px;
  }

  /* ---------- Back ---------- */
  .card--back { left: 25px; top: 515px; background: var(--card-back); }
  .card--back .brand { left: 0; right: 0; top: 118px; justify-content: center; font-size: 54px; gap: 16px; }
  .card--back .brand__dot { width: 50px; height: 50px; }
  .divider-h {
    position: absolute; left: 25px; top: 209px; width: 690px; height: 3px;
    background: linear-gradient(90deg, var(--green), var(--lime));
    border-radius: 2px;
  }
  .doctor-back {
    position: absolute; left: 0; right: 25px; top: 218px; text-align: center;
    font-family: "Exo 2", sans-serif; font-weight: 800;
    font-size: 38px; color: var(--green-name);
  }
  .email-back {
    position: absolute; left: 9px; top: 395px;
    font-size: 13px; font-weight: 500; color: var(--lime);
  }
</style>
</head>
<body>

<section class="card card--front">
  <div class="brand"><span class="brand__dot"></span>Ferncrest Dental, LLC</div>
  <div class="divider-v"></div>
  <div class="doctor-front">Dr. Lorna Pettigrew</div>

  <div class="location">
    <div class="location__label">
      <svg viewBox="0 0 10 10"><path d="M0 4h6V1l4 4-4 4V6H0z" fill="var(--orange)"/></svg>
      Location:
    </div>
    <div class="location__lines">
      2871 Marlowe Street<br>
      Bethlehem, PA 18093
    </div>
  </div>

  <div class="arrows-art" role="img" aria-label="Cluster of rising orange arrows"></div>
  <div class="band"></div>
  <div class="contact-strip">
    <span>tel.: 610-555-0193</span>
    <span>e.mail: ferncrestdental.office@examplemail.test</span>
  </div>
</section>

<section class="card card--back">
  <div class="brand"><span class="brand__dot"></span>Ferncrest Dental, LLC</div>
  <div class="divider-h"></div>
  <div class="doctor-back">Dr. Lorna Pettigrew</div>
  <div class="email-back">ferncrestdental.office@examplemail.test</div>
</section>

</body>
</html>
```